B2B flyer solution for charging infrastructures (One-Pager Din A4, double-sided)

We need a professional design for our flyer in format Din A4/both sides.
Attached you will find the content for the flyer, but we are looking for a modern, professional design.

Some background/context information:
- the product is about a solution for charging and billing of charging infrastructures (for electric cars) in companies
- target group: companies, esp. facility managers, fleet managers, controlling, CTO, CEO
- should be printed and available online
- our website (and most of our current design work): https://wendo-kraft.de

In the files you will find:
- photos of reference implementations of our solution (should be included in the flyer)
- stock photos (we are using the one you will find in the current flyer on our presentations, maybe you can use it too to keep some corporate identity.
- our logo
- the current flyer as PDF and as PowerPoint
- a sample presentation we also need for customer communication

It would be nice if the design will align with the existing design work, but bring fresh aspects and will be up-to-date and professional.

Target Market(s)

B2B, companies, fleet managers, facility managers, CTO, CIO

Industry/Entity Type

Enterprises, Charging Solutions for Electric Vehicles

Requirements
Nice to have
• Bright, light design, clean, readable

```html
<!DOCTYPE html>
<html lang="de">
<head>
<meta charset="utf-8">
<title>wendo-kraft Professional – Flyer</title>
<link rel="stylesheet" href="https://fonts.googleapis.com/css2?family=Open+Sans:wght@400;600;700;800&display=swap">
<style>
:root{
  --bg:#a9a9ab;
  --paper:#ffffff;
  --ink:#1d1d26;
  --navy:#1b1c2c;
  --magenta:#c62fb2;
  --purple:#7650c8;
  --violet:#8a46c6;
  --grad:linear-gradient(90deg,#7a55cc 0%,#b23ab8 60%,#d2309f 100%);
  --grad-v:linear-gradient(180deg,#7e52cc 0%,#b03cba 55%,#d8329c 100%);
}
*{box-sizing:border-box;margin:0;padding:0}
html,body{width:1200px;height:1177px;overflow:hidden}
body{background:var(--bg);font-family:"Open Sans",Arial,sans-serif;color:var(--ink);position:relative}
.page{position:absolute;top:234px;width:546px;height:768px;background:var(--paper);overflow:hidden}
.page--front{left:38px}
.page--back{left:612px}
.abs{position:absolute}
.photo{position:absolute;border-radius:14px}
.logo-box{position:absolute;top:0;background:var(--paper);display:flex;align-items:flex-end;justify-content:center;padding-bottom:14px}
.logo-name{font-weight:600;font-size:24px;color:var(--ink);letter-spacing:-.3px;white-space:nowrap}
.title{font-weight:800;font-size:30px;letter-spacing:-.3px;line-height:1;white-space:nowrap}
.title .brand{color:var(--magenta)}
.title .product{color:var(--purple)}
.subtitle{font-weight:700;font-size:13px;color:var(--ink);white-space:nowrap}
.intro{font-size:12.5px;line-height:16.5px}
.intro strong{color:var(--purple);font-weight:700}
.dark-panel{position:absolute;background:var(--navy);border-top-left-radius:28px}
.pill{position:absolute;border-radius:16px;color:#fff;font-weight:700;text-align:center;background:var(--grad);white-space:nowrap}
.pill--outlined{border:2px solid #e04fc4}
.services{position:absolute;list-style:none;color:#fff;font-size:10.2px;line-height:13px}
.services li{display:flex;gap:9px;align-items:flex-start;margin-bottom:9px}
.services li:last-child{margin-bottom:0}
.svc-icon{flex:none;width:24px;height:24px;border-radius:7px;background:var(--grad);display:flex;align-items:center;justify-content:center}
.ticks{position:absolute;list-style:none;color:#fff;font-size:9.3px;line-height:16px}
.ticks li{display:flex;gap:6px;align-items:center;white-space:nowrap}
.contact-cta{position:absolute;font-size:12px;line-height:15px}
.contact-cta strong{color:var(--magenta)}
.contact-bar{position:absolute;left:17px;top:710px;width:511px;height:30px;border-radius:15px;background:var(--grad);display:flex;justify-content:space-around;align-items:center;color:#fff;font-weight:700;font-size:12.5px;white-space:nowrap}
.contact-bar span{display:flex;align-items:center;gap:7px}
.c-icon{width:20px;height:20px;border-radius:50%;background:#fff;display:flex;align-items:center;justify-content:center}
.footer{position:absolute;left:0;top:746px;width:546px;height:22px;background:var(--navy);color:#d8d8e2;font-size:9.5px;text-align:center;line-height:22px}
.sec-pill{position:absolute;left:17px;width:320px;height:22px;border-radius:11px;background:var(--grad);color:#fff;font-weight:700;font-size:10.5px;line-height:22px;padding-left:14px;white-space:nowrap}
.sec-text{position:absolute;left:28px;width:310px;font-size:9.6px;line-height:12.4px}
.sec-text ul{list-style:none;font-weight:700}
.sec-text li::before{content:"";display:inline-block;width:5px;height:5px;border-radius:50%;background:var(--magenta);margin-right:5px;vertical-align:middle}
.sidebar{position:absolute;left:358px;top:210px;width:170px;height:500px;background:var(--grad-v)}
.side-head{position:absolute;left:0;top:20px;width:170px;text-align:center;color:#fff;font-size:13.5px;line-height:17px}
.target{position:absolute;left:24px;width:120px;height:74px;background:#0d0d12;border-radius:6px;color:#fff;font-size:10px;line-height:11.5px;text-align:center;display:flex;flex-direction:column;align-items:center;justify-content:flex-end;padding-bottom:6px;gap:5px}
</style>
</head>
<body>

<section class="page page--front">
  <div class="photo" style="left:17px;top:14px;width:511px;height:199px;background:linear-gradient(120deg,#dfe6f2 0%,#9fb4e6 35%,#3d62d8 60%,#6a8ef0 100%)" role="img" aria-label="Ladestecker an einem Elektroauto mit blau leuchtender Ladebuchse"></div>
  <div class="logo-box" style="left:0;width:210px;height:96px;border-bottom-right-radius:22px">
    <span class="logo-name">wendo-kraft.de</span>
  </div>

  <div class="title abs" style="left:17px;top:228px"><span class="brand">wendo-kraft</span> <span class="product">Professional</span></div>
  <div class="subtitle abs" style="left:17px;top:264px">die maßgeschneiderte B2B-Abrechnungslösung für Elektromobilität</div>
  <p class="intro abs" style="left:17px;top:292px;width:500px">Lade-Infrastruktur-Abrechnungslösungen für Unternehmen,<br>damit Lade-Infrastruktur Erträge statt Kosten produziert.<br><strong>So wird Lade-Infrastruktur von einer Kostenstelle zu einem Profitcenter.</strong></p>

  <div class="dark-panel" style="left:252px;top:360px;width:294px;height:350px"></div>
  <div class="photo" style="left:17px;top:360px;width:229px;height:240px;background:linear-gradient(160deg,#e8e8ea 0%,#b9bcc2 45%,#6f747c 100%)" role="img" aria-label="Wandladestation mit grünem Ladekabel in einer Tiefgarage"></div>

  <div class="pill pill--outlined" style="left:307px;top:376px;width:180px;height:30px;font-size:14px;line-height:26px;letter-spacing:4px">Leistungen</div>
  <ul class="services" style="left:264px;top:422px;width:262px">
    <li><span class="svc-icon"><svg width="14" height="14" viewBox="0 0 14 14"><rect x="2" y="1" width="10" height="12" rx="1.5" fill="none" stroke="#fff" stroke-width="1.5"/><path d="M4.5 5h5M4.5 8h5" stroke="#fff" stroke-width="1.3"/></svg></span><span>Vielseitige Abrechnungsmöglichkeiten für Fuhrpark, Mitarbeiter, Partnerunternehmen, Mieter, Kunden und andere.</span></li>
    <li><span class="svc-icon"><svg width="14" height="14" viewBox="0 0 14 14"><circle cx="7" cy="7" r="5" fill="none" stroke="#fff" stroke-width="1.5"/><path d="M7 4v3l2 1.5" stroke="#fff" stroke-width="1.3" fill="none"/></svg></span><span>Full-Service-Betreuung<br>(Monitoring, Abrechnung, Benutzerbetreuung)</span></li>
    <li><span class="svc-icon"><svg width="14" height="14" viewBox="0 0 14 14"><path d="M2 7a5 5 0 0 1 9-3M12 7a5 5 0 0 1-9 3" stroke="#fff" stroke-width="1.5" fill="none"/><path d="M11 1v3H8M3 13v-3h3" stroke="#fff" stroke-width="1.3" fill="none"/></svg></span><span style="padding-top:5px">Integration in ihre Unternehmensabläufe</span></li>
    <li><span class="svc-icon"><svg width="14" height="14" viewBox="0 0 14 14"><circle cx="5" cy="4.5" r="2.2" fill="#fff"/><circle cx="10" cy="5" r="1.8" fill="#fff"/><path d="M1 12a4 4 0 0 1 8 0zM8.5 12a3 3 0 0 1 5 0z" fill="#fff"/></svg></span><span>Berücksichtigung von Eigentümer/<br>Mieter-Konstellationen</span></li>
  </ul>

  <div class="pill pill--outlined" style="left:266px;top:594px;width:264px;height:28px;font-size:11.5px;line-height:24px">Mit wendo-kraft Professional profitieren</div>
  <ul class="ticks" style="left:266px;top:632px;width:276px">
    <li><svg width="9" height="9" viewBox="0 0 10 10"><path d="M1 5l3 3 5-7" stroke="#d2309f" stroke-width="2" fill="none"/></svg>Effizienter Verwaltung von Lade-Infrastruktur</li>
    <li><svg width="9" height="9" viewBox="0 0 10 10"><path d="M1 5l3 3 5-7" stroke="#d2309f" stroke-width="2" fill="none"/></svg>Umfassende Full-Service-Betreuung</li>
    <li><svg width="9" height="9" viewBox="0 0 10 10"><path d="M1 5l3 3 5-7" stroke="#d2309f" stroke-width="2" fill="none"/></svg>Nahtloser Integration in Ihre kaufmännischen Prozesse</li>
    <li><svg width="9" height="9" viewBox="0 0 10 10"><path d="M1 5l3 3 5-7" stroke="#d2309f" stroke-width="2" fill="none"/></svg>Vielseitigen Abrechnungsmöglichkeiten</li>
  </ul>

  <p class="contact-cta" style="left:30px;top:618px;width:210px"><strong>Kontaktieren</strong> Sie uns Erfahren Sie mehr über wendo-kraft und wie wir Ihre Abrechnungsanforderungen erfüllen können. Kontaktieren Sie uns für eine kostenlose Beratung:</p>

  <div class="contact-bar">
    <span><span class="c-icon"><svg width="11" height="11" viewBox="0 0 12 12"><path d="M3 1l2 3-1.3 1.2a7 7 0 0 0 3 3L8 7l3 2-1 2C5 11 1 7 1 2z" fill="#8a46c6"/></svg></span>+49 (0) 3055 218 640</span>
    <span><span class="c-icon"><svg width="11" height="11" viewBox="0 0 12 12"><rect x="1" y="2.5" width="10" height="7" rx="1" fill="#a03cba"/><path d="M1.5 3l4.5 3.5L10.5 3" stroke="#fff" fill="none"/></svg></span>info@wendo-kraft.de</span>
    <span><span class="c-icon"><svg width="11" height="11" viewBox="0 0 12 12"><circle cx="6" cy="6" r="5" fill="none" stroke="#c4339f" stroke-width="1.3"/><path d="M1 6h10M6 1c-3 3-3 7 0 10M6 1c3 3 3 7 0 10" stroke="#c4339f" fill="none"/></svg></span>www.wendo-kraft.de</span>
  </div>
  <div class="footer">wendo-kraft - Die Abrechnungslösung für Lade-Infrastruktur in Unternehmen.</div>
</section>

<section class="page page--back">
  <div class="photo" style="left:17px;top:12px;width:511px;height:198px;background:linear-gradient(100deg,#2d2f3a 0%,#3f5fc8 35%,#8b8fa6 60%,#e7dde6 100%)" role="img" aria-label="Ladestecker mit gelbem Kabel an einer öffentlichen Ladesäule"></div>
  <div class="logo-box" style="left:336px;width:210px;height:96px;border-bottom-left-radius:22px">
    <span class="logo-name">wendo-kraft.de</span>
  </div>
  <div class="abs" style="left:240px;top:174px;width:24px;height:24px;border-radius:50%;background:var(--magenta)"></div>

  <div class="title abs" style="left:17px;top:224px;font-size:24px"><span class="brand">wendo-kraft</span> <span class="product">Professional</span></div>
  <div class="subtitle abs" style="left:17px;top:253px;font-size:12px">die Funktionen im Überblick</div>

  <div class="sec-pill" style="top:280px">Full-Service-Betreuung für sorgenfreies Management</div>
  <div class="sec-text" style="top:306px">
    <p>wendo-kraft übernimmt auf Wunsch alle organisatorischen Belange bei der Verwaltung Ihrer Lade-Infrastruktur, einschließlich:</p>
    <ul><li>Monitoring</li><li>Support</li><li>User-Onboarding und -Support</li><li>Handling von Zugangskarten</li><li>Integration von firmeninternen Zugangstoken</li></ul>
  </div>

  <div class="sec-pill" style="top:410px">Perfekte Integration in kaufmännische Prozesse</div>
  <div class="sec-text" style="top:438px">
    <p>wendo-kraft fügt sich nahtlos in die kaufmännischen Strukturen moderner Unternehmen ein und bietet:</p>
    <ul><li>Erweitertes Reporting</li><li>Aufschlüsselung und Tarifierung nach Nutzergruppe</li><li>Unterstützung unternehmensinterner Abrechnung und</li><li>Verrechnung und/oder Zahlungseinzug durch wendo-kraft</li><li>Schnittstellen zu Buchhaltung und Lohnbuchhaltung</li><li>Bedarfsgerechte Anpassbarkeit</li></ul>
  </div>

  <div class="sec-pill" style="top:559px">Besonderer Aspekt: Eigentümer-Mieter-Konstellationen</div>
  <div class="sec-text" style="top:586px">
    <p>Häufige Situation: Der Mieter eines Objektes benötigt Lade-Infrastruktur, der Eigentümer/Verwalter möchte nicht zusätzlich belastet werden.</p>
    <ul><li>Unterschiedliche Betreibermodelle für verschiedene Situationen (Langzeit-Mieter vs. Kurzzeit-Mieter)</li><li>Kauf-, Miet- und Leasing-Optionen</li><li>Kostenneutral für Eigentümer/Verwalter durch geeignete Abrechnungsmodelle</li></ul>
  </div>

  <aside class="sidebar">
    <div class="side-head">Verrechnung von<br>Ladevorgängen für:</div>
    <div class="target" style="top:58px">
      <svg width="70" height="22" viewBox="0 0 70 22"><g fill="#fff"><path d="M2 14l4-7h12l5 7h3v5H2z"/><path d="M24 14l4-7h12l5 7h3v5H24z"/><path d="M46 14l4-7h12l5 7h2v5H46z"/></g><g fill="#0d0d12"><circle cx="8" cy="19" r="2.5"/><circle cx="20" cy="19" r="2.5"/><circle cx="30" cy="19" r="2.5"/><circle cx="42" cy="19" r="2.5"/><circle cx="52" cy="19" r="2.5"/><circle cx="64" cy="19" r="2.5"/></g></svg>
      <span>Fuhrpark,<br>Dienstwagen</span>
    </div>
    <div class="target" style="top:140px">
      <svg width="44" height="28" viewBox="0 0 44 28"><g fill="#fff"><circle cx="22" cy="7" r="6"/><path d="M12 27a10 10 0 0 1 20 0z"/><circle cx="8" cy="10" r="4.5"/><path d="M0 27a8 8 0 0 1 14-5v5z"/><circle cx="36" cy="10" r="4.5"/><path d="M30 22a8 8 0 0 1 14 5H30z"/></g></svg>
      <span>Mitarbeiter<br>Privatfahrzeuge</span>
    </div>
    <div class="target" style="top:218px">
      <svg width="40" height="30" viewBox="0 0 40 30"><g fill="#fff"><circle cx="20" cy="5" r="4"/><rect x="16" y="10" width="8" height="12" rx="2"/><circle cx="9" cy="8" r="3.5"/><rect x="5.5" y="13" width="7" height="11" rx="2"/><circle cx="31" cy="8" r="3.5"/><rect x="27.5" y="13" width="7" height="11" rx="2"/><rect x="17" y="21" width="2.5" height="8"/><rect x="20.5" y="21" width="2.5" height="8"/></g></svg>
      <span>Kunden<br>und Gäste</span>
    </div>
    <div class="target" style="top:296px">
      <svg width="36" height="30" viewBox="0 0 36 30"><g fill="#fff"><rect x="2" y="10" width="10" height="20"/><rect x="13" y="2" width="11" height="28"/><rect x="25" y="14" width="9" height="16"/></g><g fill="#0d0d12"><rect x="16" y="6" width="2" height="2"/><rect x="20" y="6" width="2" height="2"/><rect x="16" y="12" width="2" height="2"/><rect x="20" y="12" width="2" height="2"/><rect x="5" y="14" width="2" height="2"/><rect x="5" y="20" width="2" height="2"/><rect x="28" y="18" width="2" height="2"/></g></svg>
      <span>Vermieter,<br>Eigentümer</span>
    </div>
    <div class="photo" style="left:12px;top:378px;width:146px;height:110px;border-radius:4px;background:linear-gradient(150deg,#8a7f74 0%,#5f6b5b 50%,#3d4a3f 100%)" role="img" aria-label="Wandladestationen mit grünen Kabeln an einer Hausfassade"></div>
  </aside>

  <div class="contact-bar">
    <span><span class="c-icon"><svg width="11" height="11" viewBox="0 0 12 12"><path d="M3 1l2 3-1.3 1.2a7 7 0 0 0 3 3L8 7l3 2-1 2C5 11 1 7 1 2z" fill="#8a46c6"/></svg></span>+49 (0) 3055 218 640</span>
    <span><span class="c-icon"><svg width="11" height="11" viewBox="0 0 12 12"><rect x="1" y="2.5" width="10" height="7" rx="1" fill="#a03cba"/><path d="M1.5 3l4.5 3.5L10.5 3" stroke="#fff" fill="none"/></svg></span>info@wendo-kraft.de</span>
    <span><span class="c-icon"><svg width="11" height="11" viewBox="0 0 12 12"><circle cx="6" cy="6" r="5" fill="none" stroke="#c4339f" stroke-width="1.3"/><path d="M1 6h10M6 1c-3 3-3 7 0 10M6 1c3 3 3 7 0 10" stroke="#c4339f" fill="none"/></svg></span>www.wendo-kraft.de</span>
  </div>
  <div class="footer">wendo-kraft - Die Abrechnungslösung für Lade-Infrastruktur in Unternehmen.</div>
</section>

</body>
</html>
```